Quellbyte Business cards template

We're looking for something modern and elegant. We are a reseller of technology (computers, datacenter, etc). Color theme would be "only" white with the incorporation of the blue that's present on our website (Quellbyte.com) and logo file. We would like for the card to provide all the necessary info for the specific person (Phone#, fax#, email, name, website URL) . I'm attaching the logo file to this request. Please have it show Montreal/New York somewhere, without providing specific addresses.

Target Market(s)

All b2b

Industry/Entity Type

Business

Contact Information for Business Card

Please have the color scheme be represented by only the white and blue from our website (Quellbyte.com) and logo. We would like to logo on the card, but not big and overwhelming. This card will be used as a template for anybody within the company, it should display the user's name, phone#, fax#, email, job title and website URL. Please have it show Montreal/New York somewhere, without providing our specific addresses. Really, we're looking for a clean, simple and elegant look.

Font styles to use
Serif

Requirements
Must have
• Please see card details
Nice to have
• Please see card details
Should not have
• Anything tacky or tagline.

```html
<!DOCTYPE html>
<html lang="en">
<head>
<meta charset="utf-8">
<title>Quellbyte Business Card</title>
<link rel="stylesheet" href="https://fonts.googleapis.com/css2?family=Source+Serif+4:wght@400;600;700&display=swap">
<style>
  :root {
    --brand-blue: #1a7fd1;
    --deep-blue: #0f5fae;
    --text-grey: #6b6b6b;
    --card-white: #ffffff;
    --canvas-bg: #e6e8eb;
  }
  * { margin: 0; padding: 0; box-sizing: border-box; }
  html, body {
    width: 1200px; height: 864px; overflow: hidden;
    background: var(--canvas-bg);
    font-family: "Source Serif 4", Georgia, serif;
  }
  .sheet {
    width: 1200px; height: 864px;
    display: flex; flex-direction: column;
    align-items: center; justify-content: center; gap: 40px;
  }
  .card {
    position: relative;
    width: 560px; height: 320px;
    background: var(--card-white);
    border-radius: 24px;
    box-shadow: 0 6px 18px rgba(0,0,0,0.12);
  }
  .wordmark {
    font-weight: 600;
    color: var(--brand-blue);
    letter-spacing: 0.5px;
    white-space: nowrap;
  }
  .card-front .wordmark {
    position: absolute; left: 0; right: 0; top: 108px;
    text-align: center; font-size: 52px; line-height: 1.2;
  }
  .card-front .cities {
    position: absolute; left: 0; right: 0; bottom: 46px;
    text-align: center; font-size: 15px; color: var(--text-grey);
  }
  .cities .dot { margin: 0 10px; }
  .card-back .wordmark {
    position: absolute; left: 42px; top: 136px; font-size: 40px; line-height: 1.2;
  }
  .card-back .divider {
    position: absolute; left: 318px; top: 66px;
    width: 1.5px; height: 188px; background: var(--brand-blue);
  }
  .contact {
    position: absolute; left: 340px; top: 86px; right: 20px;
    color: var(--text-grey); font-size: 13px; line-height: 1.5;
  }
  .contact .name { color: var(--deep-blue); font-weight: 700; font-size: 20px; line-height: 1.2; }
  .contact .title { font-size: 13.5px; margin-bottom: 14px; }
  .contact .line { display: flex; align-items: center; gap: 7px; white-space: nowrap; }
  .contact svg { width: 12px; height: 12px; flex: none; }
</style>
</head>
<body>
<main class="sheet">
  <section class="card card-front">
    <div class="wordmark">Quellbyte</div>
    <div class="cities">Montreal<span class="dot">•</span>New York</div>
  </section>

  <section class="card card-back">
    <div class="wordmark">Quellbyte</div>
    <div class="divider"></div>
    <div class="contact">
      <div class="name">Alex Morgan</div>
      <div class="title">President</div>
      <div class="line">
        <svg viewBox="0 0 12 12" fill="none" stroke="#1a7fd1" stroke-width="1.6"><path d="M3 1.5 L4.5 4 L3.5 5 Q5 7.5 7 8.5 L8 7.5 L10.5 9 L9.5 10.5 Q4 10 1.5 3 Z"/></svg>
        <span>1-855-555-QUEL (7835)</span>
      </div>
      <div class="line">
        <svg viewBox="0 0 12 12" fill="none" stroke="#1a7fd1" stroke-width="1.3"><rect x="3" y="1.5" width="6" height="3"/><rect x="1.5" y="4.5" width="9" height="4.5"/><rect x="3" y="7.5" width="6" height="3"/></svg>
        <span>1-000-000-0000</span>
      </div>
      <div class="line">
        <svg viewBox="0 0 12 12" fill="none" stroke="#1a7fd1" stroke-width="1.2"><rect x="1" y="2.5" width="10" height="7"/><path d="M1 2.5 L6 6.5 L11 2.5"/></svg>
        <span>info@quellbyte.com</span>
      </div>
      <div class="line">
        <svg viewBox="0 0 12 12" fill="none" stroke="#1a7fd1" stroke-width="1.1"><circle cx="6" cy="6" r="5"/><ellipse cx="6" cy="6" rx="2.2" ry="5"/><path d="M1 6 H11"/></svg>
        <span>Quellbyte.com</span>
      </div>
    </div>
  </section>
</main>
</body>
</html>
```